BrightForge /

We need a logo and letterhead for a startup Dental Laboratory in New Zealand. The business makes things like dentures, crowns, implants and night guards on prescription from dentists. The appliances are fabricated then shipped back to the dentist who recalls the patient and fits them. We are looking for a minimilist, very professional design. We don't want any play on words or mention of smiles or anything to do with apples. Would like the name to read
"BrightForge" and then a tag line " Innovative Laboratory Solutions"
Not that fussed on a logo other than maybe BF. The final design should communicate contemporary professionalism, innovation and an eye for detail.

```html
<!DOCTYPE html>
<html lang="en">
<head>
<meta charset="utf-8">
<title>BrightForge Letterhead</title>
<link href="https://fonts.googleapis.com/css2?family=Montserrat:wght@700&family=Kumbh+Sans:wght@400&display=swap" rel="stylesheet">
<style>
  :root {
    --navy: #1d3a6b;
    --green: #7dbb3c;
    --paper: #f7f7f7;
    --backdrop: #e6e4e0;
    --ink: #1a1a1a;
    --wash-navy: rgba(29, 58, 107, 0.07);
    --wash-green: rgba(125, 187, 60, 0.06);
  }
  * { margin: 0; padding: 0; box-sizing: border-box; }
  html, body {
    width: 1189px;
    height: 1200px;
    overflow: hidden;
    background: var(--backdrop);
  }
  .stage {
    position: relative;
    width: 1189px;
    height: 1200px;
  }
  .letterhead {
    position: absolute;
    left: 131px;
    top: 0;
    width: 912px;
    height: 1181px;
    background: var(--paper);
    transform: scale(1.016);
    transform-origin: top left;
    overflow: hidden;
  }
  .brand {
    position: absolute;
    left: 76px;
    top: 76px;
    display: flex;
    align-items: center;
    gap: 22px;
  }
  .brand-dot {
    width: 104px;
    height: 104px;
    border-radius: 50%;
    background: var(--navy);
    flex: none;
  }
  .brand-text { display: flex; flex-direction: column; }
  .brand-name {
    font-family: "Montserrat", sans-serif;
    font-weight: 700;
    font-size: 58px;
    line-height: 1;
    color: var(--navy);
    letter-spacing: 1px;
  }
  .brand-tagline {
    margin-top: 12px;
    font-family: "Montserrat", sans-serif;
    font-weight: 700;
    font-size: 13.5px;
    letter-spacing: 4.6px;
    text-transform: uppercase;
    color: var(--ink);
  }
  .watermark {
    position: absolute;
    left: -40px;
    top: 230px;
    width: 820px;
    height: 820px;
    border-radius: 50%;
    background: radial-gradient(circle at 55% 45%, var(--wash-navy) 0%, var(--wash-green) 45%, rgba(247,247,247,0) 70%);
  }
  .footer {
    position: absolute;
    left: 76px;
    top: 1072px;
    width: 760px;
  }
  .footer-rule {
    height: 6px;
    background: var(--navy);
  }
  .contact-row {
    display: flex;
    align-items: center;
    margin-top: 14px;
    font-family: "Kumbh Sans", sans-serif;
    font-size: 16px;
    line-height: 19px;
    color: var(--ink);
  }
  .contact-group { display: flex; flex-direction: column; }
  .contact-line { display: flex; align-items: center; gap: 10px; white-space: nowrap; }
  .contact-line svg { width: 12px; height: 12px; flex: none; }
  .divider {
    width: 2px;
    height: 34px;
    background: var(--green);
    margin: 0 38px;
  }
  .address { margin-left: -2px; }
</style>
</head>
<body>
<div class="stage">
  <div class="letterhead">
    <header class="brand">
      <div class="brand-dot"></div>
      <div class="brand-text">
        <span class="brand-name">BrightForge</span>
        <span class="brand-tagline">Innovative Laboratory Solutions</span>
      </div>
    </header>

    <div class="watermark" role="img" aria-label="Faint brand watermark area"></div>

    <footer class="footer">
      <div class="footer-rule"></div>
      <div class="contact-row">
        <div class="contact-group">
          <div class="contact-line">
            <svg viewBox="0 0 12 12" aria-hidden="true"><path d="M2.5 0.5 L4.5 0.5 L5 3.5 L3.6 4.4 C4.3 6 5.8 7.6 7.6 8.4 L8.5 7 L11.5 7.5 L11.5 9.5 C11.5 10.8 10.5 11.5 9.5 11.5 C4.5 11 1 7.5 0.5 2.5 C0.5 1.4 1.3 0.5 2.5 0.5 Z" fill="var(--green)"/></svg>
            <span>123 456 7890</span>
          </div>
          <div class="contact-line">
            <svg viewBox="0 0 12 12" aria-hidden="true"><rect x="3" y="0.5" width="6" height="3" fill="var(--green)"/><rect x="0.5" y="4" width="11" height="5" rx="1" fill="var(--green)"/><rect x="3" y="8" width="6" height="3.5" fill="var(--green)" stroke="var(--paper)" stroke-width="0.8"/></svg>
            <span>123 456 7890</span>
          </div>
        </div>
        <div class="divider"></div>
        <div class="contact-group">
          <div class="contact-line">
            <svg viewBox="0 0 12 12" aria-hidden="true"><rect x="0.5" y="2" width="11" height="8" fill="var(--green)"/><path d="M0.5 2 L6 6.5 L11.5 2" fill="none" stroke="var(--paper)" stroke-width="1"/></svg>
            <span>company@youremail.com</span>
          </div>
          <div class="contact-line">
            <svg viewBox="0 0 12 12" aria-hidden="true"><circle cx="6" cy="6" r="5.5" fill="var(--green)"/><path d="M0.5 6 H11.5 M6 0.5 V11.5 M6 0.5 C3 3 3 9 6 11.5 M6 0.5 C9 3 9 9 6 11.5" fill="none" stroke="var(--paper)" stroke-width="0.7"/></svg>
            <span>www.yourcompanyweb.com</span>
          </div>
        </div>
        <div class="divider"></div>
        <div class="contact-group address">
          <span>234 Your Address, 2nd Street</span>
          <span>Kingwood, 1234, New Zealand</span>
        </div>
      </div>
    </footer>
  </div>
</div>
</body>
</html>
```